Harvest Bridge Christian Ministry needs a Conference Ad

We are a Christian nonprofit focused on eliminating systemic poverty and helping believers function as ministers in their workplaces. The 2025 Lantern Path Global Conference coming up in October, and we need an ad for social media (facebook, instagram, and X) and our website in order to get people excited to attend! We are looking for a modern and sleek design that incorporates our logo (attached file). You can either put just the butterfly and then write our company name separately somewhere in the design or use it as is (we used Gotham font for the logo). We want to emphasize the joy of in-person connection at the conference, so you could possibly include stock photos of young people gathering together. You could also include the attached photo of our founders in the design and say “with Mel and Dora Quintavan". Also, include the conference dates, which are October 9-12, 2025, and say “come in person or join online”. Lastly, please include the tagline “from the Pellmore Awakening to Worldwide Transformation”. NOTE: I’m attaching AN EXAMPLE I’ve created of how the design could look, which you can feel free to use for inspiration.
Young people on Instagram and facebook
- Gotham

```html
<!DOCTYPE html>
<html lang="en">
<head>
<meta charset="utf-8">
<title>Lantern Path Global Conference 2025 – Ad</title>
<link href="https://fonts.googleapis.com/css2?family=Montserrat:ital,wght@0,300;0,400;0,500;0,600;0,700;1,600&family=Oswald:wght@500;600&display=swap" rel="stylesheet">
<style>
  :root {
    --page: #eef1f6;
    --navy-deep: #0d2458;
    --navy: #18346f;
    --navy-mid: #2b4a86;
    --sky-haze: #5b77a8;
    --white: #ffffff;
    --ink: #1b2a55;
    --photo-warm: #8a7a5c;
    --photo-green: #4f6b45;
    --photo-dark: #2b2b33;
  }
  * { margin: 0; padding: 0; box-sizing: border-box; }
  html, body {
    width: 675px; height: 1200px; overflow: hidden;
    background: var(--page);
  }
  .ad {
    position: absolute; left: 25px; top: 292px;
    width: 625px; height: 616px;
    overflow: hidden;
    color: var(--white);
    font-family: "Montserrat", sans-serif;
  }
  .ad__backdrop {
    position: absolute; inset: 0;
    background:
      linear-gradient(180deg, var(--navy-deep) 0%, rgba(24,52,111,0.85) 22%, rgba(43,74,134,0.75) 55%, var(--navy) 82%, var(--navy-deep) 100%),
      linear-gradient(90deg, var(--navy-mid), var(--sky-haze) 60%, var(--navy-mid));
  }
  .ad__graphics { position: absolute; inset: 0; }

  .brand {
    position: absolute; left: 30px; top: 27px;
    display: flex; align-items: center; gap: 10px;
    font-size: 16.5px; font-weight: 500; letter-spacing: 0.02em;
    text-transform: uppercase; white-space: nowrap;
  }
  .brand__dot {
    width: 22px; height: 22px; border-radius: 50%;
    background: var(--white);
  }

  .headline {
    position: absolute; right: 29px; top: 140px;
    text-align: right; text-transform: uppercase;
  }
  .headline__big {
    display: block;
    font-family: "Oswald", sans-serif; font-weight: 600;
    line-height: 1; letter-spacing: -0.005em;
  }
  .headline__top { font-size: 42px; }
  .headline__small {
    display: block; margin: 4px 0 2px;
    font-size: 15px; font-style: italic; font-weight: 600;
  }
  .headline__bottom { font-size: 56px; }

  .hosts {
    position: absolute; right: 29px; top: 396px;
    text-align: right; text-transform: uppercase;
    font-size: 19px; font-weight: 300; line-height: 22.5px;
    letter-spacing: 0.03em;
  }

  .band {
    position: absolute; left: 0; right: 0; bottom: 0; height: 96px;
    background: linear-gradient(180deg, rgba(13,36,88,0) 0%, rgba(13,36,88,0.9) 35%, var(--navy-deep) 100%);
  }
  .dates {
    position: absolute; left: 31px; top: 541px;
    text-transform: uppercase; font-size: 19px; line-height: 18px;
    letter-spacing: 0.02em;
  }
  .dates__month { display: block; font-weight: 400; }
  .dates__days { display: block; font-weight: 600; }

  .attend-pill {
    position: absolute; left: 155px; top: 541px;
    width: 167px; height: 50px; border-radius: 25px;
    background: var(--white); color: var(--ink);
    display: flex; flex-direction: column; justify-content: center;
    padding-left: 17px;
    text-transform: uppercase; font-size: 14px; line-height: 15px;
    font-weight: 400; letter-spacing: 0.01em;
  }

  .tagline {
    position: absolute; right: 29px; top: 551px;
    text-align: left; text-transform: uppercase;
    font-size: 14.5px; line-height: 17px; letter-spacing: 0.02em;
  }
  .tagline__lead { display: block; font-weight: 400; }
  .tagline__end { display: block; font-size: 12.5px; font-weight: 400; }
  .tagline__end strong { font-weight: 700; }
</style>
</head>
<body>
  <main class="ad">
    <div class="ad__backdrop" role="img" aria-label="City skyline across a river at dusk, tinted deep blue"></div>

    <svg class="ad__graphics" width="625" height="616" viewBox="0 0 625 616" aria-hidden="false">
      <defs>
        <radialGradient id="groupPhoto" cx="45%" cy="55%" r="65%">
          <stop offset="0%" stop-color="#8d8068"/>
          <stop offset="55%" stop-color="#56684a"/>
          <stop offset="100%" stop-color="#2b2b33"/>
        </radialGradient>
        <radialGradient id="foundersPhoto" cx="45%" cy="50%" r="65%">
          <stop offset="0%" stop-color="#9a7d6a"/>
          <stop offset="60%" stop-color="#3a3a42"/>
          <stop offset="100%" stop-color="#1c1c22"/>
        </radialGradient>
      </defs>

      <path class="orbit-arc" d="M345 129 A187 187 0 1 0 77 368" fill="none" stroke="#ffffff" stroke-width="1.4" stroke-opacity="0.85"/>
      <circle cx="345" cy="129" r="5" fill="#ffffff"/>
      <circle cx="77" cy="368" r="5" fill="#ffffff"/>

      <circle class="photo-group" cx="211" cy="250" r="161" fill="url(#groupPhoto)" role="img" aria-label="Photo of four young friends laughing together outdoors"/>
      <circle class="photo-founders" cx="385" cy="430" r="98" fill="url(#foundersPhoto)" role="img" aria-label="Photo of founders Mel and Dora Quintavan"/>

      <circle cx="43" cy="404" r="12" fill="#ffffff"/>
      <circle cx="135" cy="452" r="5.5" fill="#ffffff"/>
      <circle cx="248" cy="451" r="17" fill="#ffffff"/>
    </svg>

    <div class="brand">
      <span class="brand__dot"></span>
      <span class="brand__name">Lantern Path Global Conference 2025</span>
    </div>

    <h1 class="headline">
      <span class="headline__big headline__top">Transformation</span>
      <span class="headline__small">Happens</span>
      <span class="headline__big headline__bottom">Together</span>
    </h1>

    <p class="hosts">With Mel<br>and Dora<br>Quintavan</p>

    <div class="band"></div>

    <p class="dates">
      <span class="dates__month">October</span>
      <span class="dates__days">9-12, 2025</span>
    </p>

    <p class="attend-pill">
      <span>Come in person</span>
      <span>or join online</span>
    </p>

    <p class="tagline">
      <span class="tagline__lead">From the Pellmore Awakening</span>
      <span class="tagline__end">to <strong>Worldwide Transformation</strong></span>
    </p>
  </main>
</body>
</html>
```